4th Generation Family Business Needs a New Card Design!

We are a family owned 4th Generation company. We are based in the Sydney, Australia area and we are desperately in need of a more modern and classy card. We are monumental masons who design, supply & erect lasting memorials throughout cemeteries in Sydney. Our customers are normally in a period of grieving. I have attached logo files that will need to be implemented on the card. Company was established 1935. Australian Owned and Operated. Card needs to be designed to PRINTLY.com specification.

Target Market(s)

Our target market is based upon people that a grieving for family members that have passed away. We also deal with alot of companies that own and operate cemeteries.

Industry/Entity Type

Business

Contact Information for Business Card

Oliver Brantley, Operations Manager, 0417552908, oliver@hollowaystoneworks.com.au
Martin Brantley, Director, 0431906627, martin@hollowaystoneworks.com.au
Phone # 02 9634 2258
Website: www.hollowaystoneworks.com.au
Address: Suite 17, 8 Calloway Lane, East Penrose, Sydney NSW 2290

Font styles to use
Serif
Decorative
Script

Requirements
Must have
• Would like to see the logo nicely implemented with a modern design. Embossed lettering would be a nice additive.

```html
<!DOCTYPE html>
<html lang="en">
<head>
<meta charset="utf-8">
<title>Holloway Stoneworks – Business Card</title>
<link rel="stylesheet" href="https://fonts.googleapis.com/css2?family=Cinzel:wght@500&family=Open+Sans:wght@400&display=swap">
<style>
  :root {
    --backdrop: #4a3a3e;
    --card-dark: #231f20;
    --card-light: #ffffff;
    --gold: #ecbd2f;
    --ink: #231f20;
    --text-light: #ffffff;
  }
  html, body {
    margin: 0;
    width: 1200px;
    height: 1200px;
    overflow: hidden;
    background: var(--backdrop);
  }
  .canvas {
    position: relative;
    width: 1200px;
    height: 1200px;
  }
  .card {
    position: absolute;
    left: 256px;
    width: 688px;
    height: 390px;
    box-shadow: 0 6px 14px rgba(0,0,0,0.45);
    overflow: hidden;
  }
  .card-front {
    top: 190px;
    background: var(--card-dark);
  }
  .card-back {
    top: 621px;
    background: var(--card-light);
  }
  .brand {
    position: absolute;
    font-family: "Cinzel", serif;
    font-weight: 500;
    text-align: center;
    line-height: 1;
    margin: 0;
  }
  .brand-front {
    left: 0;
    right: 0;
    top: 135px;
    color: var(--gold);
  }
  .brand-front .brand-main { display: block; font-size: 58px; letter-spacing: 1px; }
  .brand-front .brand-sub { display: block; font-size: 27px; letter-spacing: 2px; margin-top: 10px; }
  .brand-back {
    left: 40px;
    width: 220px;
    top: 160px;
    color: var(--ink);
  }
  .brand-back .brand-main { display: block; font-size: 33px; }
  .brand-back .brand-sub { display: block; font-size: 16px; letter-spacing: 1px; margin-top: 6px; }
  .back-panel {
    position: absolute;
    inset: 0;
    width: 688px;
    height: 390px;
  }
  .contact {
    position: absolute;
    right: 60px;
    top: 124px;
    text-align: right;
    font-family: "Open Sans", sans-serif;
    color: var(--text-light);
  }
  .contact-name {
    margin: 0;
    font-size: 24px;
    line-height: 30px;
    color: var(--gold);
    font-weight: 400;
  }
  .contact-role {
    margin: 0;
    font-size: 16px;
    line-height: 22px;
  }
  .contact-list {
    list-style: none;
    margin: 24px 0 0;
    padding: 0;
  }
  .contact-list li,
  .contact-address {
    display: flex;
    justify-content: flex-end;
    align-items: center;
    font-size: 16px;
    line-height: 23px;
  }
  .contact-list svg,
  .contact-address svg {
    width: 16px;
    height: 16px;
    margin-left: 10px;
    flex: none;
  }
  .contact-address {
    margin-top: 21px;
    align-items: center;
  }
  .contact-address span { display: block; }
</style>
</head>
<body>
<main class="canvas">

  <section class="card card-front" aria-label="Card front">
    <h1 class="brand brand-front">
      <span class="brand-main">HOLLOWAY</span>
      <span class="brand-sub">STONEWORKS</span>
    </h1>
  </section>

  <section class="card card-back" aria-label="Card back">
    <svg class="back-panel" viewBox="0 0 860 487" preserveAspectRatio="none" aria-hidden="true">
      <path fill="var(--gold)" d="M430 0 L860 0 L860 487 L295 487 L340 472 L340 160 C380 150 392 110 392 70 L430 54 Z"/>
      <path fill="var(--card-dark)" d="M520 0 L860 0 L860 487 L358 487 L358 170 C400 160 440 125 445 86 L445 34 C470 18 495 8 520 0 Z"/>
    </svg>

    <h2 class="brand brand-back">
      <span class="brand-main">HOLLOWAY</span>
      <span class="brand-sub">STONEWORKS</span>
    </h2>

    <div class="contact">
      <p class="contact-name">Martin Brantley</p>
      <p class="contact-role">Director</p>
      <ul class="contact-list">
        <li>0431906627
          <svg viewBox="0 0 16 16"><rect x="4" y="1" width="8" height="14" rx="1.5" fill="none" stroke="var(--gold)" stroke-width="1.6"/><circle cx="8" cy="12.5" r="0.9" fill="var(--gold)"/></svg>
        </li>
        <li>02 9634 2258
          <svg viewBox="0 0 16 16"><path fill="var(--gold)" d="M1 6 C1 2 15 2 15 6 L15 7.5 L11.5 7.5 L11.5 5.8 C9.5 5 6.5 5 4.5 5.8 L4.5 7.5 L1 7.5 Z M3 9 L13 9 L14 14 L2 14 Z"/><circle cx="8" cy="11.3" r="1.6" fill="var(--card-dark)"/></svg>
        </li>
        <li>martin@hollowaystoneworks.com.au
          <svg viewBox="0 0 16 16"><rect x="1" y="3.5" width="14" height="9" fill="var(--gold)"/><path d="M1 3.5 L8 9 L15 3.5 M1 12.5 L6 8 M15 12.5 L10 8" fill="none" stroke="var(--card-dark)" stroke-width="1"/></svg>
        </li>
        <li>www.hollowaystoneworks.com.au
          <svg viewBox="0 0 16 16" fill="none" stroke="var(--gold)" stroke-width="1.1"><circle cx="8" cy="8" r="6.5"/><ellipse cx="8" cy="8" rx="3" ry="6.5"/><path d="M1.5 8 H14.5 M2.5 4.8 H13.5 M2.5 11.2 H13.5 M8 1.5 V14.5"/></svg>
        </li>
      </ul>
      <div class="contact-address">
        <div>
          <span>Suite 17, 8 Calloway Lane</span>
          <span>East Penrose, Sydney NSW 2290</span>
        </div>
        <svg viewBox="0 0 16 16"><path fill="var(--gold)" d="M8 0.5 C4.5 0.5 2.5 3 2.5 6 C2.5 10 8 15.5 8 15.5 C8 15.5 13.5 10 13.5 6 C13.5 3 11.5 0.5 8 0.5 Z"/><circle cx="8" cy="6" r="2.2" fill="var(--card-dark)"/></svg>
      </div>
    </div>
  </section>

</main>
</body>
</html>
```